massage therapy Business Card Design

massage therapy business card
I would like a custom logo created as well.
My vision is angel wings with the WB business initials in between them.
A very simple design.
Colors preferred are light blues and greens.

Target Market(s)

Massage, Spa, fitness

Industry/Entity Type

Massage Therapy

Contact Information for Business Card

A Willow Breeze
Mara Quint
Massage Therapist and Flowing Pulse Method Practitioner
2718 Bramblewood Lane, Conway, AR 72034
501-384-6190
mara.willowbreeze@mailnest.example

Colors
abd036
33a6d7
3176b5
0255a3
0392cd
9bcb3c
cadf82

Requirements
Must have
• the logo must have angel wing.

```html
<!DOCTYPE html>
<html lang="en">
<head>
<meta charset="utf-8">
<title>A Willow Breeze – Business Card</title>
<link rel="stylesheet" href="https://fonts.googleapis.com/css2?family=Cinzel:wght@400&family=Source+Sans+3:wght@400;600&display=swap">
<style>
  :root {
    --backdrop: #141414;
    --card-white: #ffffff;
    --brand-green: #62b946;
    --brand-green-deep: #4f9e37;
    --ink-dark: #3a3a3a;
    --ink-grey: #7a7a7a;
  }
  * { margin: 0; padding: 0; box-sizing: border-box; }
  html, body {
    width: 1200px; height: 900px; overflow: hidden;
    background: var(--backdrop);
  }
  .stage { position: relative; width: 1200px; height: 900px; }
  .card {
    position: absolute; top: 170px; width: 347px; height: 561px;
  }
  .card--front { left: 259px; background: var(--card-white); }
  .card--back { left: 631px; background: var(--brand-green); }

  .accent-bar {
    position: absolute; left: 102px; width: 143px; background: var(--brand-green);
  }
  .accent-bar--top { top: 0; height: 30px; }
  .accent-bar--bottom { bottom: 0; height: 28px; }

  .front-content {
    position: absolute; inset: 0;
    font-family: "Source Sans 3", sans-serif;
    text-align: center;
  }
  .brand-mark {
    position: absolute; top: 100px; left: 50%; transform: translateX(-50%);
    width: 62px; height: 62px; border-radius: 50%; background: var(--brand-green);
  }
  .brand-name {
    position: absolute; top: 205px; left: 0; right: 0;
    font-family: "Cinzel", serif; font-size: 30px; font-weight: 400;
    color: var(--ink-dark); letter-spacing: 0.5px;
  }
  .person-name {
    position: absolute; top: 267px; left: 0; right: 0;
    font-size: 24px; font-weight: 600; color: var(--brand-green);
  }
  .person-role {
    position: absolute; top: 298px; left: 0; right: 0;
    font-size: 16px; line-height: 20px; color: var(--ink-grey);
  }
  .address {
    position: absolute; top: 364px; left: 0; right: 0;
    font-size: 16px; line-height: 21px; color: var(--ink-grey);
  }
  .contact {
    position: absolute; left: 0; right: 0;
    font-size: 16px; color: var(--ink-grey);
    display: flex; justify-content: center; align-items: center; gap: 7px;
  }
  .contact--phone { top: 429px; }
  .contact--email { top: 452px; font-size: 15px; }
  .contact svg { width: 12px; height: 12px; fill: var(--brand-green); flex: none; }

  .back-name {
    position: absolute; top: 50%; left: 0; right: 0; transform: translateY(-50%);
    text-align: center;
    font-family: "Cinzel", serif; font-size: 30px; font-weight: 400;
    color: var(--brand-green-deep);
  }
</style>
</head>
<body>
<div class="stage">
  <section class="card card--front">
    <div class="accent-bar accent-bar--top"></div>
    <div class="front-content">
      <div class="brand-mark" aria-hidden="true"></div>
      <div class="brand-name">A Willow Breeze</div>
      <div class="person-name">Mara Quint</div>
      <div class="person-role">Massage Therapist and Flowing Pulse<br>Method Practitioner</div>
      <div class="address">2718 Bramblewood Lane,<br>Conway, AR 72034</div>
      <div class="contact contact--phone">
        <svg viewBox="0 0 24 24" aria-hidden="true"><path d="M6.6 10.8a15.1 15.1 0 0 0 6.6 6.6l2.2-2.2a1 1 0 0 1 1-.25 11.4 11.4 0 0 0 3.6.57 1 1 0 0 1 1 1V20a1 1 0 0 1-1 1A17 17 0 0 1 3 4a1 1 0 0 1 1-1h3.5a1 1 0 0 1 1 1c0 1.25.2 2.45.57 3.6a1 1 0 0 1-.25 1z"/></svg>
        <span>501-384-6190</span>
      </div>
      <div class="contact contact--email">
        <svg viewBox="0 0 24 24" aria-hidden="true"><path d="M2 5h20v14H2z M2 5l10 8 10-8" fill="var(--brand-green)"/><path d="M3 6l9 7 9-7" fill="none" stroke="#fff" stroke-width="1.6"/></svg>
        <span>mara.willowbreeze@mailnest.example</span>
      </div>
    </div>
    <div class="accent-bar accent-bar--bottom"></div>
  </section>

  <section class="card card--back">
    <div class="back-name">A Willow Breeze</div>
  </section>
</div>
</body>
</html>
```